COMMERCIAL REAL ESTATE FLYER TEMPLATE

We need a template flyer designed that we can use for a current commercial real estate listing and subsequently use as a template for future listings. We have uploaded images and files to provide an example of an older flyer template we have used. If you have questions or would like to discuss, please contact us at Wade@TLMVX.net. Colors selected should be in line with our attached business card and logo design. Output should be 8.5" X 11".

Target Market(s)

Commercial Real Estate. NO RESIDENTIAL. Needs to have a professional commercial presentation with no reference to residential real estate.

Industry/Entity Type

Real Estate Agent

Font styles to use
Serif

Colors

Designer to choose colors to be used in the design.

Requirements
Must have
• MUST BE SAVED AND ADJUSTABLE IN ONE OF THE FOLLOWING FORMATES: MICROSOFT POWERPOINT, PUBLISHER OR WORD. THIS IS IMPORTANT SO OUR TEAM CAN EASILLY UPDATE TEMPLATE IN READILLY AVAILABLE PROGRAMS THAT ARE SIMPLE FOR TEAM MEMBERS TO USE.
Nice to have
• Needs to have first page template with header and footer displaying our logo, address, phone, email address and contact information for the listing agent. There need to be placeholders that can be easily adjusted based on specific listings. Placeholders will be used for pictures or aerials as the case requires. Needs to have a second page that has header and footer with a clean open block in the middle of the page so agents can customize with site specific details.
Should not have
• There should be no reference to residential. We are a commercial real estate organization that does not do any residential.

```html
<!DOCTYPE html>
<html lang="en">
<head>
<meta charset="utf-8">
<title>Flex Industrial – For Lease or Sale</title>
<link href="https://fonts.googleapis.com/css2?family=Oswald:wght@400;500;600;700&family=Pathway+Gothic+One&display=swap" rel="stylesheet">
<style>
  :root{
    --brand-red:#c4202b;
    --navy:#1f2333;
    --ink:#1a1a1a;
    --paper:#ffffff;
    --photo-warm:#b9a27a;
    --photo-dark:#6d5a40;
    --plan-peach:#f6cfa8;
    --plan-blue:#a9d8ea;
  }
  *{margin:0;padding:0;box-sizing:border-box}
  html,body{width:834px;height:1200px;overflow:hidden;background:var(--paper)}
  .flyer{position:relative;width:834px;height:1200px;font-family:"Pathway Gothic One",sans-serif;color:var(--ink)}
  .abs{position:absolute}

  .brand-block{left:8px;top:20px;width:112px;height:92px;background:var(--brand-red);color:#fff;
    font-family:"Oswald",sans-serif;font-weight:600;display:flex;flex-direction:column;justify-content:flex-end;padding:0 0 8px 12px;line-height:1.05}
  .brand-block .brand-name{font-size:22px;letter-spacing:1px;margin-bottom:6px}
  .brand-block .brand-sub{font-size:8px;letter-spacing:.2px}

  .frame-top{left:120px;top:66px;width:670px;height:3px;background:var(--brand-red)}
  .frame-right{left:786px;top:66px;width:3px;height:724px;background:var(--brand-red)}

  .hero-photo{left:357px;top:83px;width:405px;height:282px;background:linear-gradient(160deg,#cdbb94 0%,var(--photo-warm) 45%,#e5dcc6 100%)}

  .property-type{left:25px;top:150px;font-family:"Oswald",sans-serif;font-weight:600;font-size:38px;color:var(--brand-red);letter-spacing:.3px}
  .contact{left:23px;top:212px;font-size:17px;line-height:23px}
  .contact h3{font-family:"Oswald",sans-serif;font-weight:600;font-size:16px;color:var(--brand-red);margin-bottom:4px}

  .address-bar{left:0;top:367px;width:789px;height:38px;background:var(--navy);color:#fff;
    font-family:"Oswald",sans-serif;font-weight:600;font-size:24px;text-align:right;padding-right:14px;line-height:38px}
  .offer-bar{left:0;top:405px;width:789px;height:80px;background:var(--brand-red);color:#fff;
    font-family:"Oswald",sans-serif;font-weight:500;font-size:52px;text-align:right;padding-right:12px;line-height:96px}

  .thumb{top:530px;width:148px;height:98px}
  .thumb-1{left:8px;background:linear-gradient(135deg,#d8cdb5,#a89168)}
  .thumb-2{left:163px;background:linear-gradient(135deg,#e2dccd,#8a6a45)}
  .thumb-3{left:318px;background:linear-gradient(135deg,#e6dfcf,var(--photo-dark))}

  .highlights{left:470px;top:541px;width:306px;text-align:right}
  .highlights .lead{font-family:"Oswald",sans-serif;font-weight:600;font-size:17px}
  .highlights .sub{color:var(--brand-red);font-size:19px;line-height:22px;text-align:center;margin-top:10px}

  .floor-plan{left:8px;top:685px;width:226px;height:385px;
    background:linear-gradient(180deg,var(--plan-blue) 0%,var(--plan-blue) 20%,var(--plan-peach) 24%,var(--plan-peach) 100%);border:1px solid #999}
  .plan-note{left:8px;top:1072px;width:226px;text-align:center;font-size:9px;line-height:10px;font-family:"Oswald",sans-serif;color:#444}

  .specs{left:273px;top:646px;width:330px;font-size:16px;line-height:19.5px}
  .specs .row{display:flex}
  .specs dt{width:230px;color:var(--brand-red);font-family:"Oswald",sans-serif;font-weight:600;font-size:13.5px}
  .specs dd{font-size:15px}

  .section-head{top:800px;height:30px;color:#fff;font-family:"Oswald",sans-serif;font-weight:600;font-size:25px;line-height:30px;padding-left:4px}
  .office-head{left:248px;width:193px;background:var(--brand-red)}
  .warehouse-head{left:497px;width:216px;background:var(--navy)}
  .feature-list{top:838px;list-style:none;font-size:16px;line-height:19.6px}
  .office-list{left:251px}
  .warehouse-list{left:505px}

  .config-tab{left:740px;top:787px;width:72px;height:306px;background:var(--brand-red);display:flex;align-items:center;justify-content:center}
  .config-tab span{writing-mode:vertical-rl;color:#fff;font-family:"Oswald",sans-serif;font-weight:600;font-size:34px;letter-spacing:1px}

  .disclaimer{left:10px;top:1106px;width:814px;text-align:center;font-family:"Oswald",sans-serif;font-size:9.6px;line-height:13.5px;color:#222}
</style>
</head>
<body>
<div class="flyer">
  <div class="abs brand-block">
    <div class="brand-name">TLMVX</div>
    <div class="brand-sub">COMMERCIAL REAL ESTATE</div>
  </div>
  <div class="abs frame-top"></div>
  <div class="abs frame-right"></div>

  <div class="abs hero-photo" role="img" aria-label="Photo of the tech supervision room with projector screen and computer desk"></div>

  <h1 class="abs property-type">FLEX INDUSTRIAL</h1>
  <div class="abs contact">
    <h3>CONTACT</h3>
    <p>Wade S. Thornton</p>
    <p>President | CEO</p>
    <p>Phone: (281) 555-0147</p>
    <p>E-Mail: Wade@TLMVX.net</p>
    <p>TREC Broker License: 9004471</p>
  </div>

  <div class="abs address-bar">18350 Ridgeline Blvd., Houston, Texas 77073</div>
  <div class="abs offer-bar">For Lease or Sale</div>

  <div class="abs thumb thumb-1" role="img" aria-label="Photo of the executive office"></div>
  <div class="abs thumb thumb-2" role="img" aria-label="Photo of a private office with desk"></div>
  <div class="abs thumb thumb-3" role="img" aria-label="Photo of the break room kitchen"></div>

  <div class="abs highlights">
    <p class="lead">Well Maintained Owner-Occupied Building</p>
    <p class="sub">Great Location Near IAH &amp; The Woodlands.<br>Easy Access to Hardy, IH-45 &amp; Beltway 8</p>
  </div>

  <div class="abs floor-plan" role="img" aria-label="Floor plan showing office rooms above approximately 9,000 SF warehouse space with three grade-level doors"></div>
  <p class="abs plan-note">Map for representation purposes only<br>Not to Scale</p>

  <dl class="abs specs">
    <div class="row"><dt>Year of Construction</dt><dd>2006</dd></div>
    <div class="row"><dt>Building Area</dt><dd>11,820 SF (HCAD)</dd></div>
    <div class="row"><dt>Land Area</dt><dd>41,616 SF (HCAD)</dd></div>
    <div class="row"><dt>Office Area (Approx)</dt><dd>2,820 SF (Owner)</dd></div>
    <div class="row"><dt>Warehouse Area (Arpprox)</dt><dd>9,000 SF (Owner)</dd></div>
  </dl>

  <div class="abs section-head office-head">OFFICE</div>
  <div class="abs section-head warehouse-head">WAREHOUSE</div>

  <ul class="abs feature-list office-list">
    <li>(1) 14’ X 16’ Executive Office</li>
    <li>(2) 14’ X 12’ Offices</li>
    <li>(1) 10’8” X 12’ Office</li>
    <li>(1) Women’s Restroom</li>
    <li>(1) Men’s Restroom</li>
    <li>(1) Unisex Restroom</li>
    <li>(1) 21’11” X 13’ Conference Room</li>
    <li>(1) Approximately 29’ X 20’ Training Room</li>
    <li>(1) 26’ X 11’ Expanded Copy/Work Room</li>
    <li>(1) 14’ X 18’8” Break Room</li>
    <li>(1) 16’ X 12’ Tech Supervision Room</li>
    <li>(Multiple) Storage Closets</li>
  </ul>
  <ul class="abs feature-list warehouse-list">
    <li>(3) Grade-Level Loading Doors</li>
    <li>Approximately 22’ Eave Height</li>
    <li>3-Phase Power</li>
    <li>Room For Fenced Outside Storage</li>
    <li>Plenty of Parking</li>
    <li>Large Dumpster Enclosure</li>
  </ul>

  <div class="abs config-tab"><span>CONFIGURATIONS</span></div>

  <p class="abs disclaimer">The information contained herein has, we believe, been obtained from reliable sources, and we have no reason to doubt the accuracy thereof. All such information is submitted, subject to errors, omissions or changes in condition prior to sale, lease or withdrawal without notice. All information contained herein should be verified by the person relying thereon. We have not made and will not make any warranty or representation as to the condition of the property nor the presence of any hazardous substances or any environmental or other conditions that may affect the value or suitability of the property.</p>
</div>
</body>
</html>
```